Business Card Design for a coaching and consulting company (usage of existing logo)

We need a business card design for a new business start up (coaching & consulting) incorporating an existing logo that has just been created by a tallomira designer.

The business card should pick up the existing logo and its colours (please check out variations as well) and look fresh, light, open and professional. The business card must be applicable for worldwide clients and must adhere to the standard Australian business card measurements. We are open for fun designs that require special print techniques as long as it doesn't get too expensive/fancy in the print process. We prefer versions that use both sides of the business card as we personally find 1-siders a little bit boring.

Business

```html
<!DOCTYPE html>
<html lang="en">
<head>
<meta charset="utf-8">
<title>Harborline – Business Card</title>
<link rel="stylesheet" href="https://fonts.googleapis.com/css2?family=Open+Sans:wght@400;600&display=swap">
<style>
  :root {
    --backdrop: #b3b3b3;
    --card-white: #ffffff;
    --brand-yellow: #f8c832;
    --brand-grey: #4a4a4c;
    --text-grey: #555557;
  }
  * { box-sizing: border-box; margin: 0; padding: 0; }
  html, body {
    width: 1200px; height: 960px; overflow: hidden;
    background: var(--backdrop);
    font-family: "Open Sans", Arial, sans-serif;
  }
  .card {
    position: absolute; left: 320px;
    width: 560px; height: 342px;
    overflow: hidden;
    box-shadow: 0 6px 18px rgba(0,0,0,.18);
  }
  .card--front { top: 90px; background: var(--card-white); }
  .card--back  { top: 528px; background: var(--brand-yellow); }

  .brand { position: absolute; display: flex; align-items: center; gap: 12px; }
  .brand__dot { width: 22px; height: 22px; border-radius: 50%; }
  .brand__name { font-weight: 600; font-size: 34px; letter-spacing: -0.5px; }
  .card--front .brand { left: 40px; top: 124px; }
  .card--front .brand__dot { background: var(--brand-yellow); }
  .card--front .brand__name { color: var(--brand-grey); }
  .card--back .brand { left: 50%; top: 112px; transform: translateX(-50%); }
  .card--back .brand__dot { background: var(--card-white); }
  .card--back .brand__name { color: var(--brand-grey); }

  .identity {
    position: absolute; left: 316px; top: 48px;
    border-left: 3px solid var(--brand-yellow); padding-left: 10px;
  }
  .identity__name { color: var(--brand-yellow); font-size: 22px; line-height: 1.1; }
  .identity__role { color: var(--text-grey); font-size: 13px; margin-top: 6px; }

  .contact { position: absolute; left: 316px; top: 138px; list-style: none; color: var(--text-grey); font-size: 13px; }
  .contact li { display: flex; align-items: flex-start; gap: 9px; line-height: 1.5; }
  .contact li.gap { margin-top: 12px; }
  .contact svg { flex: none; width: 12px; height: 12px; margin-top: 4px; fill: var(--brand-yellow); }

  .bands { position: absolute; left: 0; top: 0; width: 560px; height: 342px; }

  .web-line {
    position: absolute; left: 0; right: 0; top: 214px;
    display: flex; justify-content: center; align-items: center; gap: 8px;
    color: var(--brand-grey); font-size: 13px; font-weight: 600;
  }
  .web-line svg { width: 12px; height: 12px; fill: var(--card-white); }
</style>
</head>
<body>

<section class="card card--front">
  <svg class="bands" viewBox="0 0 560 342" aria-hidden="true">
    <polygon points="312,290 560,268 560,281 300,303" fill="var(--brand-yellow)"/>
    <polygon points="0,316 292,292 280,304 0,328" fill="var(--brand-grey)"/>
  </svg>

  <div class="brand"><span class="brand__dot"></span><span class="brand__name">Harborline</span></div>

  <div class="identity">
    <p class="identity__name">Your Name</p>
    <p class="identity__role">Coaching &amp; Condulting</p>
  </div>

  <ul class="contact">
    <li>
      <svg viewBox="0 0 12 12"><path d="M6 0a4 4 0 0 0-4 4c0 3 4 8 4 8s4-5 4-8a4 4 0 0 0-4-4zm0 5.5A1.5 1.5 0 1 1 6 2.5a1.5 1.5 0 0 1 0 3z"/></svg>
      <span>Meridian Court, Quay Lane,<br>Westbrook.</span>
    </li>
    <li class="gap">
      <svg viewBox="0 0 12 12"><path d="M3 0h6v12H3zM4 1.5v8h4v-8z"/></svg>
      <span>000 - 555 - 0142</span>
    </li>
    <li>
      <svg viewBox="0 0 12 12"><path d="M0 2h12v8H0zM1 3l5 3.5L11 3z" fill-rule="evenodd"/></svg>
      <span>your@mailbox.com</span>
    </li>
    <li>
      <svg viewBox="0 0 12 12"><circle cx="6" cy="6" r="6"/></svg>
      <span>www.yourdomain.com</span>
    </li>
  </ul>
</section>

<section class="card card--back">
  <div class="brand"><span class="brand__dot"></span><span class="brand__name">Harborline</span></div>

  <p class="web-line">
    <svg viewBox="0 0 12 12"><circle cx="6" cy="6" r="6"/></svg>
    <span>www.yourdomain.com</span>
  </p>

  <svg class="bands" viewBox="0 0 560 342" aria-hidden="true">
    <polygon points="0,296 290,302 300,312 0,306" fill="var(--card-white)"/>
    <polygon points="310,308 560,314 560,324 320,318" fill="var(--brand-grey)"/>
  </svg>
</section>

</body>
</html>
```